Business Card Design

I am a medical doctor who is also trained in eastern medicine and acupuncture. I would like to incorporate the chinese characters for "Balance" in a vertical configuration, prominently featured on the left hand side of the card. (see image that I tried to cut and paste together. There is also a horizontal version, but I would like the characters stacked. I included each character separately) I would like the chinese characters and my name to be in blue or teal with the other print either brown or black. I would like this tag line on the back of the card: "Balancing Western and Eastern Medicine to Achieve Optimal Health". I tried out a similar design in Cardquill Templates but the chinese characters said "sushi". Not exactly appropriate. Many thanks.

Industry/Entity Type

Medical

Contact Information for Business Card

Margaret Delane, MD, LAc
582-B Pohaku St
Makalei, HI 96792
(808) 471-2096
margaretMDneedlework@mailbrook.example
www.margaretMDneedlework.example

```html
<!DOCTYPE html>
<html lang="en">
<head>
<meta charset="utf-8">
<title>Margaret Delane, MD, LAc — Business Card</title>
<link href="https://fonts.googleapis.com/css2?family=Jost:wght@400;500&display=swap" rel="stylesheet">
<style>
  :root {
    --navy: #262c64;
    --navy-soft: #2f3673;
    --name-blue: #2d3275;
    --ink: #111111;
    --paper: #ffffff;
    --backdrop: #dfe0e2;
    --swirl-dark: #3b3f8f;
    --swirl-light: #3aa6dc;
  }
  html, body {
    margin: 0;
    padding: 0;
    width: 1200px;
    height: 1000px;
    overflow: hidden;
    background: var(--backdrop);
  }
  .canvas {
    position: relative;
    width: 1200px;
    height: 1000px;
    font-family: "Jost", "Futura", sans-serif;
    color: var(--ink);
  }
  .card {
    position: absolute;
    background: var(--paper);
  }
  .card--front { left: 43px; top: 24px; width: 800px; height: 456px; }
  .card--back  { left: 348px; top: 495px; width: 799px; height: 468px; }

  .calligraphy-band {
    position: absolute;
    left: 15px; top: 15px;
    width: 198px; height: 428px;
    background: linear-gradient(180deg, var(--navy) 0%, var(--navy-soft) 50%, var(--navy) 100%);
  }
  .name {
    position: absolute;
    left: 213px; right: 0; top: 24px;
    margin: 0;
    text-align: center;
    font-weight: 400;
    font-size: 52px;
    line-height: 60px;
    color: var(--name-blue);
    letter-spacing: 0.5px;
  }
  .credentials {
    position: absolute;
    left: 213px; right: 0; top: 100px;
    text-align: center;
    font-size: 26px;
  }
  .ornament {
    position: absolute;
    border-radius: 50%;
    background: radial-gradient(ellipse at center, var(--swirl-light) 0%, var(--swirl-dark) 45%, rgba(59,63,143,0.15) 75%, rgba(255,255,255,0) 100%);
  }
  .ornament--front { left: 452px; top: 154px; width: 108px; height: 47px; }
  .ornament--back  { left: 327px; top: 295px; width: 143px; height: 68px; }

  .email {
    position: absolute;
    left: 284px; top: 260px;
    font-size: 24px;
  }
  .address {
    position: absolute;
    left: 284px; top: 341px;
    font-size: 24px;
    line-height: 36px;
    font-style: normal;
  }
  .divider {
    position: absolute;
    left: 504px; top: 341px;
    width: 2px; height: 80px;
    background: var(--ink);
  }
  .phone-web {
    position: absolute;
    left: 523px; top: 340px;
  }
  .phone { font-size: 26px; line-height: 36px; }
  .web { font-size: 17px; line-height: 20px; }

  .tagline {
    position: absolute;
    left: 0; right: 0; top: 160px;
    margin: 0;
    text-align: center;
    font-weight: 400;
    font-size: 31px;
    line-height: 44px;
  }
</style>
</head>
<body>
<main class="canvas">
  <section class="card card--front" aria-label="Card front">
    <div class="calligraphy-band" role="img" aria-label="Vertical band with brush calligraphy characters meaning balance"></div>
    <h1 class="name">Margaret Delane</h1>
    <div class="credentials">MD, LAc</div>
    <div class="ornament ornament--front" role="img" aria-label="Blue flourish ornament"></div>
    <div class="email">margaretMDneedlework@mailbrook.example</div>
    <address class="address">582-B Pohaku St<br>Makalei, HI 96792</address>
    <div class="divider"></div>
    <div class="phone-web">
      <div class="phone">(808) 471-2096</div>
      <div class="web">margaretMDneedlework.example</div>
    </div>
  </section>

  <section class="card card--back" aria-label="Card back">
    <h2 class="tagline">Balancing Western and Eastern<br>Medicine to Achieve Optimal Health</h2>
    <div class="ornament ornament--back" role="img" aria-label="Blue flourish ornament"></div>
  </section>
</main>
</body>
</html>
```